Business Card Design

We require a business card design for a law firm, our signature colours are maroon and cream. Our slogan is "From our family to yours", we would like the cards to be professional however feminine at the same time.

Industry/Entity Type

Business

Contact Information for Business Card

Helena Brackett & Associates Lawyers & Conveyancers, Helena Brackett LL.B. Principal Solicitor, 17 Quillon Street, Marrowdale NSW 2190

Logo styles of interest
Emblem Logo
Abstract Logo
Wordmark Logo

```html
<!DOCTYPE html>
<html lang="en">
<head>
<meta charset="utf-8">
<title>Helena Brackett &amp; Associates – Business Card</title>
<link href="https://fonts.googleapis.com/css2?family=Crimson+Text:wght@400&family=Roboto+Slab:wght@300;700&display=swap" rel="stylesheet">
<style>
  :root {
    --maroon: #8e1b1f;
    --cream: #f9df93;
    --backdrop: #3b3b3d;
  }
  * { margin: 0; padding: 0; box-sizing: border-box; }
  html, body {
    width: 991px;
    height: 1200px;
    overflow: hidden;
    background: var(--backdrop);
  }
  .card {
    position: absolute;
    left: 195px;
    top: 121px;
    width: 600px;
    height: 958px;
    background: var(--cream);
    border-radius: 40px;
    overflow: hidden;
    color: var(--maroon);
    text-align: center;
  }
  .brand-mark {
    position: absolute;
    left: 172px;
    top: 68px;
    width: 256px;
    height: 256px;
    background: var(--maroon);
    border-radius: 34px;
  }
  .firm-name {
    position: absolute;
    top: 340px;
    left: 0;
    width: 100%;
    font-family: "Crimson Text", Georgia, serif;
    font-size: 35px;
    line-height: 1.2;
  }
  .firm-type {
    position: absolute;
    top: 388px;
    left: 0;
    width: 100%;
    display: flex;
    justify-content: center;
    align-items: center;
    gap: 18px;
    font-family: "Crimson Text", Georgia, serif;
    font-size: 28px;
  }
  .firm-type .rule {
    width: 64px;
    height: 2px;
    background: var(--maroon);
  }
  .slogan-band {
    position: absolute;
    top: 490px;
    left: 0;
    width: 100%;
    height: 50px;
    background: var(--maroon);
    color: var(--cream);
    font-family: "Roboto Slab", Georgia, serif;
    font-weight: 300;
    font-size: 31px;
    line-height: 50px;
  }
  .contact {
    position: absolute;
    top: 668px;
    left: 0;
    width: 100%;
  }
  .contact-name {
    font-family: "Roboto Slab", Georgia, serif;
    font-weight: 700;
    font-size: 35px;
    line-height: 50px;
  }
  .contact-details {
    margin-top: 26px;
    font-family: "Roboto Slab", Georgia, serif;
    font-weight: 300;
    font-size: 26px;
    line-height: 39px;
  }
  .footer-tab {
    position: absolute;
    left: 119px;
    bottom: 0;
    width: 363px;
    height: 18px;
    background: var(--maroon);
    border-radius: 5px 5px 0 0;
  }
</style>
</head>
<body>
  <div class="card">
    <div class="brand-mark" aria-hidden="true"></div>
    <div class="firm-name">Helena Brackett &amp; Associates</div>
    <div class="firm-type"><span class="rule"></span>Lawyers<span class="rule"></span></div>
    <div class="slogan-band">From Our Family To Yours</div>
    <div class="contact">
      <div class="contact-name">Helena Brackett</div>
      <div class="contact-details">
        LL.B. Principal Solicitor,<br>
        17 Quillon Street,<br>
        Marrowdale NSW 2190
      </div>
    </div>
    <div class="footer-tab"></div>
  </div>
</body>
</html>
```